Qorvane Management LLC Business Card

The sample logo was attached for the business Card Design for Traffic Control Company named Qorvane Management LLC. Card design needs to have the company logo and colors match the logo color. It will be nice to show some images of Traffic control signs or cones, even roads closer that math the company services

Target Market(s)

Temporary traffic control. Road closer.

Industry/Entity Type

Construction

Contact Information for Business Card

basic information, name, job title, address, email phone, website

Font styles to use
Serif
Sans Serif

Colors
F0912C
F2A743
F7CA91
FBE8D2
FDF5EE
EE7325
F08F49
F5BC92
FAE3D3
FDF4ED

```html
<!DOCTYPE html>
<html lang="en">
<head>
<meta charset="utf-8">
<title>Qorvane Management LLC Business Card</title>
<link href="https://fonts.googleapis.com/css2?family=Montserrat:wght@400;500;700&display=swap" rel="stylesheet">
<style>
  :root {
    --bg: #9b9b9b;
    --card: #ffffff;
    --orange: #ee7325;
    --ink: #1f1f1f;
    --cone-a: #f08f49;
    --cone-b: #fae3d3;
  }
  * { box-sizing: border-box; margin: 0; padding: 0; }
  html, body { width: 1160px; height: 1200px; overflow: hidden; }
  body { background: var(--bg); font-family: "Montserrat", sans-serif; color: var(--ink); position: relative; }

  .card {
    position: absolute; left: 199px; width: 777px; height: 442px;
    background: var(--card); border-radius: 26px;
  }
  .card-front { top: 105px; }
  .card-back { top: 634px; }

  .wordmark { position: absolute; color: var(--orange); font-weight: 700; line-height: 1; }
  .wordmark .name { display: block; }
  .wordmark .suffix { display: block; letter-spacing: 0.12em; }

  .card-front .wordmark { left: 57px; top: 150px; width: 360px; }
  .card-front .wordmark .name { font-size: 64px; letter-spacing: 0.02em; }
  .card-front .wordmark .suffix { font-size: 24px; margin-top: 18px; }

  .divider { position: absolute; left: 457px; top: 97px; width: 2px; height: 224px; background: var(--orange); }

  .contact { position: absolute; left: 488px; top: 92px; }
  .person-name { font-size: 24px; font-weight: 700; color: var(--orange); letter-spacing: 0.01em; }
  .person-title { font-size: 18px; margin-top: 8px; }
  .address { font-size: 18px; line-height: 28px; margin-top: 14px; }
  .contact-list { list-style: none; margin-top: 14px; }
  .contact-list li { display: flex; align-items: center; gap: 14px; font-size: 19px; height: 31px; }
  .contact-list svg { width: 20px; height: 20px; fill: var(--orange); flex: none; }

  .tagline { position: absolute; left: 0; right: 0; top: 348px; text-align: center; font-size: 18px; font-weight: 500; }

  .equipment-art {
    position: absolute; left: 184px; top: 34px; width: 419px; height: 119px; border-radius: 8px;
    background: linear-gradient(90deg, var(--cone-b), var(--cone-a) 30%, var(--cone-b) 50%, var(--cone-a) 70%, var(--cone-b));
  }
  .card-back .wordmark { left: 185px; top: 200px; width: 410px; text-align: center; }
  .card-back .wordmark .name { font-size: 74px; letter-spacing: 0.02em; }
  .card-back .wordmark .suffix { font-size: 28px; margin-top: 22px; }
</style>
</head>
<body>
  <section class="card card-front">
    <div class="wordmark">
      <span class="name">QORVANE</span>
      <span class="suffix">MANAGEMENT LLC</span>
    </div>
    <div class="divider"></div>
    <div class="contact">
      <p class="person-name">DALEN MARSH</p>
      <p class="person-title">Owner/Director</p>
      <p class="address">Corvel Plaza 2700 Ridge<br>Hollow Ave Suite 118</p>
      <ul class="contact-list">
        <li><svg viewBox="0 0 24 24"><path d="M6.6 10.8a15 15 0 0 0 6.6 6.6l2.2-2.2a1 1 0 0 1 1-.25 11.4 11.4 0 0 0 3.6.57 1 1 0 0 1 1 1V20a1 1 0 0 1-1 1A17 17 0 0 1 3 4a1 1 0 0 1 1-1h3.5a1 1 0 0 1 1 1c0 1.25.2 2.45.57 3.57a1 1 0 0 1-.25 1z"/></svg>555-214-7730</li>
        <li><svg viewBox="0 0 24 24"><path d="M2 5h20v14H2z" opacity=".85"/><path d="M2 5l10 8 10-8" fill="none" stroke="#fff" stroke-width="1.8"/></svg>info@qorvanemgmt.com</li>
        <li><svg viewBox="0 0 24 24"><circle cx="12" cy="12" r="10"/><path d="M2 12h20M12 2c3 3 3 17 0 20M12 2c-3 3-3 17 0 20" fill="none" stroke="#fff" stroke-width="1.4"/></svg>www.qorvanemgmt.com</li>
      </ul>
    </div>
    <p class="tagline">Traffic Control Company named Qorvane Management LLC.</p>
  </section>

  <section class="card card-back">
    <div class="equipment-art" role="img" aria-label="Traffic cones with danger, no-parking and arrow signs"></div>
    <div class="wordmark">
      <span class="name">QORVANE</span>
      <span class="suffix">MANAGEMENT LLC</span>
    </div>
  </section>
</body>
</html>
```